Calm Course website development

Need a website designed for a coaching business. Very high-end, luxury, professionalism, in the area of STRESS, see brief attached. I have a logo already
Updates

Slow in providing feedback

Target Market(s)

CEOs very successful men and wealthy females, high end luxury market

Industry/Entity Type

coaching

Number of Pages Required

1 page

Requirements
Must have
• Luxury look, professional, serious but warm, appealing to both sexes

```html
<!DOCTYPE html>
<html lang="en">
<head>
<meta charset="utf-8">
<title>Calm Course — Stress Coaching</title>
<link href="https://fonts.googleapis.com/css2?family=Barlow:wght@300;400;500;600;700&display=swap" rel="stylesheet">
<style>
:root{
  --ink:#231f20;
  --text:#555;
  --muted:#777;
  --soft:#f2f2f2;
  --line:#d9d9d9;
  --dark:#2b2627;
  --white:#fff;
}
*{box-sizing:border-box;margin:0;padding:0}
html,body{width:1200px;height:4375px;overflow:hidden;background:var(--white)}
body{position:relative;font-family:'Barlow',Arial,sans-serif;color:var(--ink)}
.abs{position:absolute}
.photo{position:absolute}
.btn{position:absolute;border:1.5px solid var(--ink);display:flex;align-items:center;justify-content:center;font-size:17px;letter-spacing:.5px;color:var(--ink);text-transform:uppercase}
.eyebrow{position:absolute;font-size:11px;letter-spacing:3px;color:var(--text);text-transform:uppercase}
.heading-bold{font-weight:700;font-size:38px;text-transform:uppercase;letter-spacing:.5px}
.heading-light{font-weight:300;font-size:46px}
.para{font-size:15.5px;line-height:24.5px;color:var(--text)}
.center{left:0;width:1200px;text-align:center}

/* header */
.brand-box{left:87px;top:0;width:253px;height:109px;background:var(--soft);display:flex;align-items:center;justify-content:center;gap:10px}
.brand-mark{width:14px;height:14px;background:var(--ink)}
.brand-name{font-size:17px;font-weight:600;letter-spacing:5px;text-transform:uppercase}
.topbar{top:20px;right:88px;font-size:13px;display:flex;gap:28px;align-items:center}
.topbar span{display:flex;gap:7px;align-items:center}
.nav{top:60px;left:487px;display:flex;gap:40px;font-size:16px;color:#333}

/* help cards */
.help-card{position:absolute;text-align:center;padding-top:0}
.help-card h3{font-size:20px;font-weight:700;margin-top:16px}
.help-card p{font-size:15px;line-height:25px;color:var(--text);margin:10px auto 0;width:270px}
.help-card a{display:inline-block;margin-top:10px;font-size:14px;text-decoration:underline;color:var(--ink)}
.help-card.dark{background:var(--dark);color:var(--white)}
.help-card.dark p,.help-card.dark a{color:#ddd}

/* support cards */
.support-card{position:absolute;width:244px;height:216px;background:var(--white);box-shadow:0 4px 18px rgba(0,0,0,.09);text-align:center;padding-top:24px}
.support-card h4{font-size:16px;font-weight:700;margin-top:12px}
.support-card p{font-size:15px;line-height:24px;color:var(--muted);margin:8px auto 0;width:190px}

/* situations */
.situation-label{position:absolute;width:320px;text-align:center;font-size:25px;font-weight:400;color:#333}
.underline{position:absolute;height:1px;background:var(--line)}

/* process */
.step{position:absolute;left:666px;display:flex;align-items:center;gap:24px}
.step-num{width:60px;height:60px;border-radius:50%;background:var(--soft);display:flex;align-items:center;justify-content:center;font-weight:700;font-size:26px}
.step-text{font-size:30px;font-weight:300}

/* footer */
.footer{left:0;top:4019px;width:1200px;height:356px;background:var(--dark);color:var(--white)}
.footer-col{position:absolute;top:93px}
.footer-col h5{font-size:19px;font-weight:600}
.footer-col .rule{width:178px;height:1px;background:#666;margin:12px 0 14px}
.footer-col li{list-style:none;font-size:14px;color:#ccc;line-height:26.5px}
.social{display:flex;gap:10px;justify-content:center}
.social i{width:34px;height:34px;border-radius:50%;background:var(--white);display:block}
</style>
</head>
<body>

<!-- header -->
<div class="abs brand-box"><span class="brand-mark"></span><span class="brand-name">Calm Course</span></div>
<div class="abs topbar">
  <span><svg width="13" height="10" viewBox="0 0 13 10"><rect x=".5" y=".5" width="12" height="9" fill="none" stroke="#555"/><path d="M.5 .5l6 5 6-5" fill="none" stroke="#555"/></svg>hello@calmcourse.example</span>
  <span style="font-weight:600"><svg width="12" height="12" viewBox="0 0 24 24"><path d="M6.6 10.8a15 15 0 006.6 6.6l2.2-2.2a1 1 0 011-.25 11 11 0 003.6.6 1 1 0 011 1V20a1 1 0 01-1 1A17 17 0 013 4a1 1 0 011-1h3.5a1 1 0 011 1 11 11 0 00.6 3.6 1 1 0 01-.25 1z" fill="#333"/></svg>555-014-7720</span>
</div>
<nav class="abs nav"><span>Home</span><span>Services ⌄</span><span>About</span><span>Blog</span><span>Contacts</span></nav>
<div class="btn" style="left:939px;top:53px;width:173px;height:34px;font-size:15px">Schedule a tour</div>

<!-- hero -->
<div class="eyebrow" style="left:87px;top:188px">Welcome to stress free life</div>
<div class="abs" style="left:85px;top:208px;font-size:47px;line-height:48px">
  <div style="font-weight:300">We Can Make a</div>
  <div style="font-weight:700;text-transform:uppercase">Positive Change</div>
  <div style="font-weight:300">In your Life Today!</div>
</div>
<p class="abs para" style="left:87px;top:383px;width:460px">stress is not all bad...we need stress to survive and peform at an optional level. In order to do that, you need to recognize your stressors and then control them, and put it to good use when neccsary.</p>
<div class="btn" style="left:87px;top:521px;width:264px;height:48px">Make an appointment</div>
<div class="photo" role="img" aria-label="Smiling woman in a light coat talking on a phone outdoors" style="left:600px;top:110px;width:513px;height:538px;background:linear-gradient(160deg,#8fa4c4,#c9bfb4 55%,#7d6a5d)"></div>

<!-- female / male -->
<div class="photo" role="img" aria-label="Woman in a cosy sweater holding a cup in autumn woods" style="left:87px;top:650px;width:239px;height:283px;background:linear-gradient(160deg,#4a3526,#a07b5e 60%,#6b4d3a)"></div>
<div class="photo" role="img" aria-label="Man in glasses and a dark blazer" style="left:361px;top:650px;width:239px;height:283px;background:linear-gradient(160deg,#cfd6df,#7b8594 60%,#2c3340)"></div>
<div class="situation-label" style="left:46px;top:948px;width:320px;font-size:36px;font-weight:300">Female</div>
<div class="situation-label" style="left:320px;top:948px;width:320px;font-size:36px;font-weight:300">Male</div>
<div class="underline" style="left:87px;top:1001px;width:239px"></div>
<div class="underline" style="left:361px;top:1001px;width:239px"></div>

<div class="abs" style="left:663px;top:697px;font-size:37px;font-weight:300">How Can I Help You?</div>
<div class="abs" style="left:666px;top:750px;font-size:15.5px;color:var(--text)">If you're experiencing any kind of Stress or mental illness.</div>
<svg class="abs" style="left:664px;top:797px" width="56" height="56" viewBox="0 0 56 56"><circle cx="28" cy="28" r="28" fill="#231f20"/><path d="M22 19a1.5 1.5 0 011.6.9l1.6 3.7a1.5 1.5 0 01-.4 1.7l-1.6 1.3a11 11 0 005.2 5.2l1.3-1.6a1.5 1.5 0 011.7-.4l3.7 1.6a1.5 1.5 0 01.9 1.6l-.4 2.6a1.5 1.5 0 01-1.5 1.3A16 16 0 0118.1 21.9a1.5 1.5 0 011.3-1.5z" fill="#fff"/></svg>
<div class="abs" style="left:750px;top:800px;font-size:21px;font-weight:400;line-height:26px">FEEL FREE &amp; DIAL NOW<br><b style="font-weight:700">555-014-7720</b></div>
<div class="btn" style="left:667px;top:884px;width:276px;height:48px">Fixed a meeting with me</div>

<!-- situations intro -->
<div class="abs center heading-bold" style="top:1078px">I can help you</div>
<div class="abs center heading-light" style="top:1126px">In Different Situations</div>
<p class="abs para" style="left:115px;top:1204px;width:970px;text-align:center;font-size:14px;line-height:25px">Calm Course came about due to my desire to help people lead a better and healthier life. Initially, I was involved in the fitness/body side of health. As years passed and my experience grew, I realized how important the mind was in total wellness, and that the mind is all powerful and controlling. Control the mind, control the body and achieve success. Stress can be the most debilating factor in our lives, it is the root cause of so many diseases and costs the US workplace an estimated 300 billion dollars due to loss of productivity.</p>

<!-- help cards -->
<div class="abs" style="left:87px;top:1400px;width:1026px;height:289px;background:var(--soft)"></div>
<div class="help-card" style="left:87px;top:1428px;width:341px">
  <svg width="74" height="74" viewBox="0 0 74 74" fill="none" stroke="#231f20" stroke-width="2"><rect x="14" y="4" width="26" height="12"/><circle cx="22" cy="26" r="5"/><circle cx="48" cy="26" r="5"/><path d="M12 48v-10a8 8 0 0116 0v10M38 48v-10a8 8 0 0116 0v10M6 50h62M14 50v20M60 50v20M10 70h54"/></svg>
  <h3>Counseling</h3><p>Contrary to popular belief, Lorem Ipsum is not simply random text. It has roots in a piece</p><a>Read More</a>
</div>
<div class="help-card dark" style="left:428px;top:1359px;width:342px;height:369px;padding-top:69px">
  <svg width="62" height="62" viewBox="0 0 62 62" fill="none" stroke="#fff" stroke-width="2"><path d="M20 58V46c-8-5-12-12-12-20a22 22 0 0144 0l5 9-5 2v8a4 4 0 01-4 4h-8v9"/><circle cx="30" cy="25" r="10"/><path d="M30 15v20M20 25h20"/></svg>
  <h3>Consultation</h3><p>Contrary to popular belief, Lorem Ipsum is not simply random text. It has roots in a piece</p><a>Read More</a>
</div>
<div class="help-card" style="left:770px;top:1428px;width:343px">
  <svg width="74" height="74" viewBox="0 0 74 74" fill="none" stroke="#231f20" stroke-width="2"><path d="M37 38l-12-12a8 8 0 0112-10 8 8 0 0112 10z"/><path d="M33 25h8M37 21v8"/><path d="M8 30l6 26 12 14M66 30l-6 26-12 14M14 44l10 10M60 44l-10 10"/></svg>
  <h3>Health &amp; Wellness</h3><p>Contrary to popular belief, Lorem Ipsum is not simply random text. It has roots in a piece</p><a>Read More</a>
</div>

<!-- about -->
<div class="abs" style="left:350px;top:1833px;width:219px;height:407px;background:var(--soft)"></div>
<div class="photo" role="img" aria-label="Portrait of the coach in a navy suit adjusting his cuff" style="left:134px;top:1877px;width:382px;height:321px;background:linear-gradient(150deg,#2b2a33,#6a5c58 50%,#1e2a44)"></div>
<div class="eyebrow" style="left:626px;top:1815px">Why I am</div>
<div class="abs heading-bold" style="left:624px;top:1843px">I'm Dr. Daniel Reyes</div>
<div class="abs" style="left:624px;top:1890px;font-size:42px;font-weight:300">Expert Stress Coach</div>
<p class="abs para" style="left:626px;top:1960px;width:450px">Stress is not all bad, and since we are surrounded by engulfed by stress, or it isn't going anywhere soon, we need to deal with it, and even better, channel to be an advantage/tool to perform better.</p>
<p class="abs para" style="left:626px;top:2082px;width:450px">Recognize when we are feeling stress and what is causing it, understand it, and how we react to it is the first step. Then when we sense it's coming we can deal with it, resolve it, or use it to our advantage.</p>
<div class="btn" style="left:626px;top:2213px;width:138px;height:47px">About us</div>

<!-- support -->
<div class="eyebrow" style="left:87px;top:2458px">Best support</div>
<div class="abs heading-bold" style="left:86px;top:2486px">Service and support</div>
<p class="abs para" style="left:87px;top:2550px;width:440px">Effective stress control and problem solving skills may be the only thing that will keep your head above water in the next decade. It really is becoming quite serious and so should be taken very seriously. What is your plan for the next decade? Or, will you just let stress win?</p>
<div class="btn" style="left:88px;top:2707px;width:189px;height:46px">Discover more</div>

<div class="support-card" style="left:592px;top:2364px">
  <svg width="56" height="56" viewBox="0 0 56 56" fill="none" stroke="#231f20" stroke-width="1.8"><circle cx="20" cy="24" r="8"/><path d="M6 54v-8a14 14 0 0128 0v8M32 4h20v14H40l-4 4v-4h-4z"/></svg>
  <h4>Personal Sessions</h4><p>Popular Ipsum is not simply random text. It has roots in a piece.</p>
</div>
<div class="support-card" style="left:869px;top:2390px">
  <svg width="56" height="56" viewBox="0 0 56 56" fill="none" stroke="#231f20" stroke-width="1.8"><circle cx="28" cy="12" r="6"/><path d="M20 34v-8a8 8 0 0116 0v8M6 18l4 22 10 12M50 18l-4 22-10 12"/></svg>
  <h4>Anger Management</h4><p>Popular Ipsum is not simply random text. It has roots in a piece.</p>
</div>
<div class="support-card" style="left:592px;top:2617px">
  <svg width="56" height="56" viewBox="0 0 56 56" fill="none" stroke="#231f20" stroke-width="1.8"><path d="M24 20a12 12 0 0124 0c0 8-8 10-8 18a6 6 0 01-10 4M30 20a6 6 0 0112 0M8 22a10 10 0 010 14M13 25a5 5 0 010 8"/></svg>
  <h4>Excellent Listener</h4><p>Popular Ipsum is not simply random text. It has roots in a piece.</p>
</div>
<div class="support-card" style="left:869px;top:2644px">
  <svg width="56" height="56" viewBox="0 0 56 56" fill="none" stroke="#231f20" stroke-width="2.2"><path d="M28 6L52 48H4z"/><path d="M28 20v16M28 40v3"/></svg>
  <h4>Memory &amp; Attention</h4><p>Popular Ipsum is not simply random text. It has roots in a piece.</p>
</div>

<!-- we help for -->
<div class="abs center heading-bold" style="top:2966px">We help for</div>
<div class="abs center heading-light" style="top:3013px">Overcome The Fears &amp; Obstacles In Your Life</div>
<div class="photo" role="img" aria-label="Stressed man sitting on a leather sofa, head in hand" style="left:87px;top:3126px;width:320px;height:232px;background:linear-gradient(150deg,#3b3e44,#5a4437 60%,#1f1f22)"></div>
<div class="photo" role="img" aria-label="Frustrated young woman with curly hair in an orange sweater" style="left:440px;top:3126px;width:320px;height:232px;background:linear-gradient(150deg,#c9cdd0,#8b6a55 50%,#cf5a2a)"></div>
<div class="photo" role="img" aria-label="Couple sharing a close, affectionate moment" style="left:793px;top:3126px;width:320px;height:232px;background:linear-gradient(150deg,#ece8e4,#b88a6d 55%,#f4f1ed)"></div>
<div class="situation-label" style="left:87px;top:3378px">Stress and Tension</div>
<div class="situation-label" style="left:440px;top:3378px">Anger Management</div>
<div class="situation-label" style="left:793px;top:3378px">Relationship Difficulties</div>
<div class="underline" style="left:87px;top:3433px;width:320px"></div>
<div class="underline" style="left:440px;top:3433px;width:320px"></div>
<div class="underline" style="left:793px;top:3433px;width:320px"></div>

<!-- process -->
<div class="abs" style="left:87px;top:3523px;width:218px;height:411px;background:var(--soft)"></div>
<div class="photo" role="img" aria-label="Smiling woman in a blazer in a bright office" style="left:134px;top:3569px;width:380px;height:321px;background:linear-gradient(150deg,#d8dde2,#8a6e58 45%,#3a4a63)"></div>
<div class="photo" role="img" aria-label="Woman with a coffee cup sitting in a café" style="left:384px;top:3523px;width:215px;height:217px;background:linear-gradient(150deg,#b35a2a,#2b2b2d 50%,#2a8a9a);outline:4px solid #fff"></div>
<div class="eyebrow" style="left:666px;top:3566px">How we work</div>
<div class="abs heading-bold" style="left:665px;top:3594px">An amazing process</div>
<div class="step" style="top:3666px"><span class="step-num">01</span><span class="step-text">Visit Our Web</span></div>
<div class="step" style="top:3749px"><span class="step-num">02</span><span class="step-text">Book An Appointment</span></div>
<div class="step" style="top:3832px"><span class="step-num">03</span><span class="step-text">Come To Sit With Me</span></div>

<!-- footer -->
<footer class="abs footer">
  <div class="abs" style="left:195px;top:74px;width:300px;text-align:center">
    <div style="display:flex;justify-content:center;align-items:center;gap:10px"><span style="width:14px;height:14px;background:#fff;display:block"></span><span style="font-size:19px;font-weight:600;letter-spacing:5px">CALM COURSE</span></div>
    <div style="font-size:22px;font-weight:300;margin-top:24px">555-014-7720</div>
    <div style="font-size:10px;letter-spacing:2.5px;margin-top:6px;color:#ccc">24/7 AT YOUR SERVICE</div>
    <div class="social" style="margin-top:16px"><i></i><i></i><i></i></div>
    <div style="font-size:11px;margin-top:14px;color:#ccc">© CALM COURSE 2022.</div>
  </div>
  <div class="footer-col" style="left:616px">
    <h5>Company</h5><div class="rule"></div>
    <ul><li>Customer Service</li><li>FAQs</li><li>About Us</li><li>Our Service</li><li>Why Choose Us</li><li>Our Location</li></ul>
  </div>
  <div class="footer-col" style="left:865px">
    <h5>Services</h5><div class="rule"></div>
    <ul><li>Counseling</li><li>Relationships</li><li>Life coaching</li><li>Marriage</li><li>Anxiety</li></ul>
  </div>
</footer>

</body>
</html>
```